Global Summit on Thermal Peptides

We are arranging a meeting in Finland in August: THE 8th GLOBAL SUMMIT ON THERMAL PEPTIDES IN LIFE AND HEALING - CELLULAR COPING ROUTES AND CIRCUITS.

The program and speakers are included in the Word files. The basic poster arrangement could be a little bit like in the Conference:
http://events.vorelka.org/files/posters/1483956274_17-regulators-plants.pdf

Basically only the organizers and invited speakers will be listed.

We would like to have some summery maritime background of the kind provided in the stock footage. In addition, we would include some summer views from the City of Turku. We have added a few potential University Campus views in the footage folder.

Reason: There was one design that was attractive. We wanted to extend the time available to work along the approach of this design.

Target Market(s)

Scientists in the field of cell stress research

Industry/Entity Type

Management

Requirements
Must have
• There must be the logo of our home university:
• https://www.lunvik.fi/personal/media/3991/lvenglogobasic4c.jpg
• ...somewhere down on the poster, a little bit like VRKA in the example above.
• There must also be the logo of the organizing organization Tissue Strain Global Fellowship:
• http://www.tissuestrainfellows.org/?
• All text should be readable (no light text on light background and vice versa)

```html
<!DOCTYPE html>
<html lang="en">
<head>
<meta charset="utf-8">
<title>Global Summit on Thermal Peptides</title>
<link rel="stylesheet" href="https://fonts.googleapis.com/css2?family=Cabin:wght@400;500;600;700&family=Signika:wght@600;700&display=swap">
<style>
  :root {
    --navy: #1f3461;
    --title-navy: #17325a;
    --title-green: #2c7a55;
    --lime: #a6d13c;
    --white: #ffffff;
    --teal: #2aa8a0;
    --red: #c4262e;
  }
  * { margin: 0; padding: 0; box-sizing: border-box; }
  html, body { width: 776px; height: 1200px; overflow: hidden; background: #fff; }
  .poster {
    position: relative; width: 776px; height: 1200px; overflow: hidden;
    font-family: "Cabin", sans-serif;
  }
  .sea-backdrop {
    position: absolute; inset: 0;
    background: linear-gradient(180deg, #d9ecec 0%, #c3dcd8 12%, #8ea79b 17%, #5f7561 30%, #6b7a63 50%, #566650 70%, #4b5b47 85%, #6d7a64 100%);
  }
  .headline {
    position: absolute; top: 24px; left: 0; width: 776px; text-align: center;
    font-family: "Signika", sans-serif; font-weight: 700; line-height: 1;
  }
  .headline .line-1 { color: var(--title-navy); font-size: 34px; letter-spacing: 1.5px; }
  .headline .line-1 sup { font-size: 18px; vertical-align: 14px; }
  .headline .line-2, .headline .line-3 { color: var(--title-green); font-size: 34px; letter-spacing: 1.5px; margin-top: 6px; }
  .society {
    position: absolute; top: 160px; left: 0; width: 776px; text-align: center; color: var(--white);
  }
  .society .mark-circle {
    width: 96px; height: 96px; border-radius: 50%; margin: 0 auto 14px;
    background: #3d9a8f; border: 3px solid #ffffff;
  }
  .society .name { font-size: 20px; font-weight: 700; }
  .society .tagline { font-size: 13px; font-weight: 700; margin-top: 2px; }
  .info-panel {
    position: absolute; left: 27px; top: 330px; width: 722px; height: 510px;
    background: var(--navy); border-radius: 8px; border: 1px solid #4b6292;
    color: var(--white);
  }
  .info-panel .theme {
    position: absolute; left: 30px; top: 10px; font-size: 44px; font-weight: 500; line-height: 1.12;
  }
  .info-panel .dates {
    position: absolute; left: 34px; top: 118px; font-size: 27px; font-weight: 700; color: var(--lime);
  }
  .info-panel .venue {
    position: absolute; left: 34px; top: 160px; font-size: 18px; font-weight: 600; color: var(--lime);
    padding-bottom: 6px; border-bottom: 1px solid #c9d3e4; width: 428px;
  }
  .col { position: absolute; top: 208px; font-size: 11px; line-height: 17.6px; font-weight: 500; list-style: none; }
  .col b { font-weight: 700; }
  .col-organizers { left: 12px; width: 170px; line-height: 15px; }
  .col-keynotes { left: 186px; }
  .col-speakers-a { left: 359px; top: 202px; }
  .col-speakers-b { left: 571px; top: 202px; }
  .label { color: var(--white); font-weight: 700; text-transform: uppercase; font-size: 11.5px; }
  .col-keynotes .label { color: var(--lime); }
  .col-organizers .label { margin-bottom: 3px; }
  .affil { color: var(--lime); font-weight: 500; font-size: 12px; line-height: 14px; }
  .person { font-weight: 700; font-size: 12.5px; }
  .group { margin-bottom: 7px; }
  .col li::before { content: "• "; }
  .col .label::before, .col .gap::before { content: none; }
  .gap { height: 8px; }
  .notes {
    position: absolute; left: 0; top: 432px; width: 722px; padding-left: 110px; text-align: center;
    font-size: 12px; line-height: 16px; font-weight: 600;
  }
  .notes .lime { color: var(--lime); }
  .notes .white { color: var(--white); font-size: 12.5px; }
  .city-strip { position: absolute; left: 0; top: 838px; width: 776px; height: 260px; }
  .home-university {
    position: absolute; left: 0; top: 1112px; width: 776px; text-align: center;
    color: var(--red); font-weight: 600; font-size: 13px; line-height: 15px;
  }
  .home-university .mark-square { display: block; width: 34px; height: 34px; margin: 0 auto 8px; background: var(--red); }
</style>
</head>
<body>
<div class="poster">
  <div class="sea-backdrop" role="img" aria-label="Summer sea with small wooded islands on the horizon under a pale sky"></div>

  <header class="headline">
    <div class="line-1">THE 8<sup>th</sup> GLOBAL SUMMIT</div>
    <div class="line-2">ON THERMAL PEPTIDES IN</div>
    <div class="line-3">LIFE AND HEALING</div>
  </header>

  <div class="society">
    <div class="mark-circle"></div>
    <div class="name">Tissue Strain Global Fellowship</div>
    <div class="tagline">Publishers of Strain &amp; Folding Letters</div>
  </div>

  <section class="info-panel">
    <h1 class="theme">Cellular Coping Routes<br>and Circuits</h1>
    <div class="dates">August 13-17, 2017</div>
    <div class="venue">Harborview Marina Hotel, Turku, Finland</div>

    <div class="col col-organizers">
      <div class="group">
        <div class="label">Organizer:</div>
        <div class="person">Ilse Marvik</div>
        <div class="affil">Lunvik Academy University<br>Finland</div>
      </div>
      <div class="group" style="margin-top:12px">
        <div class="label">Co-organizers:</div>
        <div class="person">Tapio Rantanen</div>
        <div class="affil">Lunvik Academy University<br>and University of Varsala<br>Finland</div>
      </div>
      <div class="group">
        <div class="person">Gregory Ashworth</div>
        <div class="affil">TSGF<br>University of Norhaven<br>USA</div>
      </div>
      <div class="group">
        <div class="person">Nadine Lefort</div>
        <div class="affil">Université Seine Rive<br>France</div>
      </div>
    </div>

    <ul class="col col-keynotes">
      <li class="label">Keynotes:</li>
      <li><b>Helen Worsley</b>, UK</li>
      <li><b>Sanna Lindqvist</b>, Denmark</li>
      <li><b>Grant Ellison</b>, USA</li>
      <li><b>Oscar Pemberton</b>, USA</li>
      <li class="gap"></li>
      <li class="label">Invited speakers include:</li>
      <li><b>Marcus Dalby</b>, USA</li>
      <li><b>Livia Teixeira</b>, Brazil</li>
      <li><b>Danielle Okafor-Reyes</b>, USA</li>
      <li><b>Nathan Whitcombe</b>, USA</li>
      <li><b>Paola Ricci</b>, Italy</li>
    </ul>

    <ul class="col col-speakers-a">
      <li><b>Yoav Shapira</b>, Israel</li>
      <li><b>Robert Kingsley</b>, USA</li>
      <li><b>Fiona Marsh-Templeton</b>, UK</li>
      <li><b>Gordon T. Ashby</b>, USA</li>
      <li><b>Élise Boutin</b>, France</li>
      <li><b>Karen Wexford</b>, USA</li>
      <li><b>Joost Verhagen</b>, The Netherlands</li>
      <li><b>Tiina-Maria Korhonen</b>, Finland</li>
      <li><b>Renata Souza</b>, Brazil</li>
      <li><b>Daniel Prescott</b>, USA</li>
      <li><b>Jonas K. Weber</b>, Germany</li>
      <li><b>Philip R. Ashcroft</b>, USA</li>
    </ul>

    <ul class="col col-speakers-b">
      <li><b>Takeshi Yamamoto</b>, Japan</li>
      <li><b>Hiroshi Sato</b>, Japan</li>
      <li><b>Neil Abernathy</b>, USA</li>
      <li><b>R. Samir Haddad</b>, USA</li>
      <li><b>Pekka T. Salminen</b>, Finland</li>
      <li><b>Caroline Fitch</b>, USA</li>
      <li><b>Chiara Morelli</b>, Italy</li>
      <li><b>Adam Brightwell</b>, USA</li>
      <li><b>Warren K. Holt</b>, USA</li>
      <li><b>Ruth Carlow</b>, USA</li>
      <li><b>Glen Osborne</b>, USA</li>
    </ul>

    <div class="notes">
      <div class="lime">Short talks and poster sessions will be organized.</div>
      <div class="lime">Students and post-docs are encouraged to apply.</div>
      <div class="white">Further information:&nbsp; www.tissuestrainfellows.org</div>
      <div class="white">Contact: ilse.marvik@lunvik.fi</div>
    </div>
  </section>

  <svg class="city-strip" viewBox="0 0 776 260" width="776" height="260">
    <defs>
      <linearGradient id="park" x1="0" y1="0" x2="0" y2="1">
        <stop offset="0" stop-color="#cfe3f2"/><stop offset="0.55" stop-color="#b9b8a8"/><stop offset="1" stop-color="#4f7f38"/>
      </linearGradient>
      <linearGradient id="tower" x1="0" y1="0" x2="0" y2="1">
        <stop offset="0" stop-color="#3d86d6"/><stop offset="0.5" stop-color="#6a8a5a"/><stop offset="1" stop-color="#2e4a24"/>
      </linearGradient>
      <linearGradient id="facade" x1="0" y1="0" x2="1" y2="0">
        <stop offset="0" stop-color="#e9e3d4"/><stop offset="0.5" stop-color="#d8a86a"/><stop offset="1" stop-color="#f1ede2"/>
      </linearGradient>
    </defs>
    <path d="M0 40 Q388 -10 776 40 L776 260 Q388 210 0 260 Z" fill="var(--teal)"/>
    <path d="M0 48 Q250 12 258 14 L258 222 Q120 226 0 240 Z" fill="url(#park)" role="img" aria-label="City park with a statue, flower beds and a stone building in summer"/>
    <path d="M270 13 Q388 6 497 10 L497 218 Q388 214 270 220 Z" fill="url(#tower)" role="img" aria-label="Cathedral bell tower framed by green trees against a blue sky"/>
    <path d="M509 11 Q700 18 776 48 L776 236 Q650 214 509 216 Z" fill="url(#facade)" role="img" aria-label="Pale yellow university building with white columns and leaves in front"/>
  </svg>

  <div class="home-university">
    <span class="mark-square"></span>
    Lunvik Academy<br>University
  </div>
</div>
</body>
</html>
```